Letterhead & Business Card Design Project

Use existing logo to create a new letterhead and business card design. Looking for something clean modern using color options of black, white and gray. The green from the logo may be used lightly as an accent color.

Target Market(s)

Professional business people

Industry/Entity Type

Business

Requirements
Must have
• Business card with front and back design using existing logo.
Nice to have
• Professional presentation
Clean look
Should not have
• No oil rigs, pumpjacks or clip art.

```html
<!DOCTYPE html>
<html lang="en">
<head>
<meta charset="utf-8">
<title>Meridian Exploration – Business Card</title>
<link rel="stylesheet" href="https://fonts.googleapis.com/css2?family=Questrial&display=swap">
<style>
  :root {
    --ink: #000000;
    --paper: #ffffff;
    --name-ink: #1a1a1a;
    --panel: #1a1b1f;
    --ghost: #38393d;
    --muted: #9a9a9a;
    --web-grey: #444444;
    --accent: #5aa85a;
  }
  * { margin: 0; padding: 0; box-sizing: border-box; }
  html, body { width: 1200px; height: 1200px; overflow: hidden; }
  body {
    position: relative;
    background: linear-gradient(to bottom, var(--ink) 0, var(--ink) 612px, var(--paper) 612px);
    font-family: "Questrial", sans-serif;
  }
  .card {
    position: absolute;
    left: 245px;
    width: 710px;
    height: 434px;
    overflow: hidden;
  }
  .card-front { top: 158px; background: var(--paper); }
  .card-back {
    top: 629px;
    background: var(--ink);
    box-shadow: 0 0 10px rgba(0, 0, 0, 0.35);
  }

  .company-name {
    position: absolute;
    left: 0;
    width: 100%;
    text-align: center;
    font-family: "Questrial", sans-serif;
    font-weight: 400;
    line-height: 1;
    white-space: nowrap;
  }
  .card-front .company-name {
    top: 178px;
    font-size: 40px;
    color: var(--name-ink);
  }
  .accent-rule {
    position: absolute;
    left: 182px;
    top: 240px;
    width: 346px;
    height: 2px;
    background: linear-gradient(to right, rgba(90, 168, 90, 0.2), var(--accent) 20%, var(--accent) 80%, rgba(90, 168, 90, 0.2));
  }

  .website {
    position: absolute;
    top: 373px;
    width: 100%;
    text-align: center;
    font-size: 16px;
    color: var(--web-grey);
  }

  .brand-panel {
    position: absolute;
    left: 30px;
    top: 0;
    width: 293px;
    height: 100%;
    background: var(--panel);
  }
  .brand-panel .company-name {
    top: 224px;
    font-size: 26px;
    color: var(--ghost);
  }

  .contact-name {
    position: absolute;
    left: 384px;
    top: 164px;
    font-size: 32px;
    font-weight: 400;
    color: var(--paper);
  }
  .contact-title {
    position: absolute;
    left: 385px;
    top: 208px;
    font-size: 18px;
    color: var(--muted);
  }
  .contact-details {
    position: absolute;
    left: 385px;
    top: 322px;
    font-size: 14px;
    line-height: 17px;
    color: var(--paper);
    list-style: none;
  }
</style>
</head>
<body>
  <section class="card card-front">
    <p class="company-name">Meridian Exploration</p>
    <div class="accent-rule"></div>
    <p class="website">www.meridianexploration.com</p>
  </section>

  <section class="card card-back">
    <div class="brand-panel">
      <p class="company-name">Meridian Exploration</p>
    </div>
    <h1 class="contact-name">Daniel R Hayes</h1>
    <p class="contact-title">Managing Member</p>
    <ul class="contact-details">
      <li>4520 North Alder Ave Suite 210 Tulsa,</li>
      <li>Oklahoma 74100</li>
      <li>Phone 555.201.4410</li>
      <li>Fax 555.201.4411</li>
      <li>Cell 555.372.9086</li>
    </ul>
  </section>
</body>
</html>
```